Brightmarket Tradehub (appstore) Billboards - Dealbeacon

We offer an app on the Brightmarket Tradehub - B2B app store which is called Dealbeacon. We have a presentation of our application consisting of 15 billboards with information and graphics about our application. I want a new design for our Billboards and want to have the first 5 created.

Here is our App listing and when you click on the big image you see the billboards I want to create. The first 5 is enough and I also want the template so I can create more myself.
I have added a ppt with lots of screenshots of the application

Each image/Billboard must follow these specs Specs: 700x467 pixel jpg or png no larger than 1MB

https://tradehub.brightmarket-example.com/listingDetail?listingId=k7R2B91100XQmzTPLV

Here is a video about what the Dealbeacon app does

Target Market(s)

Brightmarket customers , Sales Executives, VP Sales , Sales operations - Relevant for all industries that run a sales process based on customer meetings and/or phone meetings

Colors

Designer to choose colors to be used in the design.

Requirements
Must have
• Screenshots from the solution. The billboards is to spike interest from people viewing and also showcase how things look inside their Brightmarket solution with our Dealbeacon app running
• - SEE EXAMPLE Billboard image of what type of Billboard I am after

```html
<!DOCTYPE html>
<html lang="en">
<head>
<meta charset="utf-8">
<title>Dealbeacon – Different questions for different types of sales conversations</title>
<link href="https://fonts.googleapis.com/css2?family=Montserrat:wght@400;500;600;700&family=Roboto:wght@400;500&display=swap" rel="stylesheet">
<style>
  :root {
    --sky: #3b9cf2;
    --sky-light: #46a6f6;
    --navy: #0b2341;
    --white: #ffffff;
    --frame: #f1f3f5;
    --frame-edge: #d5d9de;
    --ui-text: #2b2f36;
    --ui-muted: #6b7480;
    --ui-line: #d8dde3;
    --ui-link: #1a6fb8;
    --ui-select: #1e7fe0;
    --chip: #e9eef5;
    --chip-badge: #7a5fd0;
  }
  * { box-sizing: border-box; margin: 0; padding: 0; }
  html, body { width: 1200px; height: 801px; overflow: hidden; }
  body { font-family: "Montserrat", sans-serif; background: var(--sky); }

  .billboard { position: relative; width: 1200px; height: 801px; overflow: hidden; background: var(--sky); }
  .backdrop { position: absolute; inset: 0; }

  .brand { position: absolute; left: 118px; top: 36px; display: flex; align-items: center; gap: 12px; color: var(--white); }
  .brand-dot { width: 34px; height: 34px; border-radius: 50%; background: var(--white); }
  .brand-name { font-weight: 700; font-size: 31px; letter-spacing: 0.2px; }

  .headline { position: absolute; right: 72px; top: 50px; width: 620px; text-align: right;
    color: var(--navy); font-weight: 500; font-size: 35px; line-height: 1.33; }

  .lede { position: absolute; left: 118px; top: 446px; width: 300px;
    color: var(--navy); font-weight: 500; font-size: 22px; line-height: 1.32; }

  .tablet { position: absolute; left: 408px; top: 221px; width: 736px; height: 502px;
    background: var(--frame); border: 2px solid var(--frame-edge); border-radius: 34px;
    box-shadow: 0 10px 30px rgba(11,35,65,0.25); }
  .tablet-camera { position: absolute; left: 22px; top: 245px; width: 9px; height: 9px; border-radius: 50%; background: var(--navy); }
  .tablet-button { position: absolute; right: 26px; top: 234px; width: 32px; height: 32px; border-radius: 50%; border: 2px solid #b9bfc6; background: var(--frame); }

  .screen { position: absolute; left: 56px; top: 27px; width: 576px; height: 448px; background: var(--white);
    border: 1px solid var(--frame-edge); overflow: hidden; font-family: "Roboto", sans-serif; color: var(--ui-text); }

  .browser-tabs { height: 20px; background: #dfe3e8; display: flex; align-items: flex-end; padding-left: 8px; gap: 2px; }
  .browser-tab { height: 16px; width: 96px; background: #eef1f4; border-radius: 4px 4px 0 0; font-size: 6.5px; padding: 4px 6px; color: var(--ui-muted); white-space: nowrap; overflow: hidden; }
  .browser-tab.is-active { background: var(--white); color: var(--ui-text); }
  .address-bar { height: 20px; background: var(--white); border-bottom: 1px solid var(--ui-line); display: flex; align-items: center; padding: 0 8px; gap: 6px; font-size: 6.5px; color: var(--ui-muted); }
  .address-field { flex: 1; height: 13px; border: 1px solid var(--ui-line); border-radius: 3px; padding: 2px 6px; white-space: nowrap; overflow: hidden; }
  .secure { color: #1f8a3a; }

  .page-head { padding: 7px 12px 8px; border-bottom: 1px solid var(--ui-line); background: #f7f9fb; }
  .breadcrumb { font-size: 7px; color: var(--ui-link); }
  .page-title { font-size: 10.5px; margin-top: 3px; }

  .form { position: absolute; left: 141px; top: 98px; width: 368px; padding: 8px 10px; border: 1px solid var(--ui-line); border-radius: 3px; background: var(--white); font-size: 7px; }
  .form-label { color: var(--ui-muted); font-size: 6.5px; margin-bottom: 3px; }
  .chips { display: flex; gap: 6px; margin-bottom: 5px; }
  .chip { display: flex; align-items: center; gap: 3px; background: var(--chip); border-radius: 2px; padding: 2px 4px 2px 2px; font-size: 6.5px; }
  .chip-badge { width: 10px; height: 10px; border-radius: 2px; background: var(--chip-badge); }
  .input { height: 15px; border: 1px solid var(--ui-line); border-radius: 3px; padding: 3px 6px; color: var(--ui-muted); margin-bottom: 7px; position: relative; }
  .input-icon { position: absolute; right: 6px; top: 3px; width: 7px; height: 7px; border: 1px solid var(--ui-muted); border-radius: 50%; }
  .select { height: 15px; border: 1.5px solid var(--ui-select); border-radius: 3px; padding: 3px 6px; position: relative; }
  .select::after { content: "▴▾"; position: absolute; right: 5px; top: 1px; font-size: 6px; letter-spacing: -2px; writing-mode: vertical-lr; }
  .options { list-style: none; border: 1px solid var(--ui-line); border-top: none; font-size: 6.5px; line-height: 9.6px; }
  .options li { padding: 0 4px; }
  .options li.is-selected { background: var(--ui-select); color: var(--white); }
</style>
</head>
<body>
<main class="billboard">
  <svg class="backdrop" viewBox="0 0 1200 801" width="1200" height="801" aria-hidden="true">
    <path d="M700 0 C 820 90 960 150 1200 150 L1200 0 Z" fill="var(--sky-light)"/>
    <path d="M0 0 L612 0 C 470 140 300 250 0 420 Z" fill="var(--navy)"/>
    <path d="M860 801 C 950 700 1080 580 1200 520 L1200 801 Z" fill="var(--navy)"/>
  </svg>

  <div class="brand">
    <span class="brand-dot"></span>
    <span class="brand-name">Dealbeacon</span>
  </div>

  <h1 class="headline">Different questions for different types of sales conversations.</h1>

  <p class="lede">Request feedback based on what kind of sales conversation you had with the customer/prospect.</p>

  <div class="tablet">
    <span class="tablet-camera"></span>
    <span class="tablet-button"></span>
    <div class="screen">
      <div class="browser-tabs">
        <div class="browser-tab is-active">https://demo--beacon.bm7</div>
        <div class="browser-tab">Dealbeacon: Win more deals</div>
      </div>
      <div class="address-bar">
        <span>◀ ▶ ⟳</span>
        <div class="address-field"><span class="secure">Secure</span> | https://demo--beacon.bm7.brightmarket-example.com/apex/requestFeedback?opportunity=006A100000QxR2</div>
      </div>
      <div class="page-head">
        <div class="breadcrumb">Opportunities &gt; Northwind Solar - Telecom</div>
        <div class="page-title">Request Feedback</div>
      </div>
      <form class="form">
        <div class="form-label">Recipients</div>
        <div class="chips">
          <span class="chip"><span class="chip-badge"></span>Nora Lindqvist ✕</span>
          <span class="chip"><span class="chip-badge"></span>Tomas Reyes ✕</span>
        </div>
        <div class="input">Search<span class="input-icon"></span></div>
        <div class="form-label">Survey Form</div>
        <div class="select">01 - Introduction meeting</div>
        <ul class="options">
          <li>Select a Survey</li>
          <li>01 - Introduction meeting</li>
          <li>02 - Discovery meeting</li>
          <li class="is-selected">03 - Demo meeting</li>
          <li>04 - Win evaluation</li>
          <li>05 - Negotiations</li>
          <li>06 - Client Feedback</li>
          <li>07 - Project delivery</li>
          <li>08 - Customer Satisfaction (CSAT)</li>
          <li>09 - Advisory &amp; Analyst Call Feedback</li>
          <li>10 - Informal meeting</li>
        </ul>
      </form>
    </div>
  </div>
</main>
</body>
</html>
```